We are looking for a Flyer we will send through the mail for residents of Apartment Buildings

We are a laundry service doing pickup and delivery for the Manhattan Area.
We offer next day delivery on all laundry orders.
we want to send out a flyer to buildings for unbelievable promotion:

50% your first order (coupon code FOLD50)
2nd order FREE! (up to $50)
FREE pickup and delivery
FREE next day service
FREE Brisa and Plumo
schedule now on www.quickrinsehub.com!

We offer the cleanest and brightest laundry in the city!
Attached is our logo plus some icons to use

Target Market(s)

females ages 24-40

Industry/Entity Type

Apartment

Font styles to use
Other font styles liked:
• habraba

Requirements
Must have
• modern and clean look
• our logo
• BRIGHT COLORS
• Size of flyer will be 8.52 x 5.47
• Logo font: Harabara
• Slogan font: Swiss 721 Light Extended BT
• Dark blue: C 100 M 88 Y 0 K 0
• Light blue: C 85 M 50 Y 0 K 0
• Orange: C 0 M 80 Y 95 K 0
• Violet: C 85 M 100 Y 0 K 0
Should not have
• we dont want to be too busy

```html
<!DOCTYPE html>
<html lang="en">
<head>
<meta charset="utf-8">
<title>QuickRinseHub Flyer</title>
<link rel="stylesheet" href="https://fonts.googleapis.com/css2?family=Montserrat:wght@300;600&family=Open+Sans:ital,wght@0,400;0,700;1,400&family=Fira+Sans+Condensed:wght@500;600&display=swap">
<style>
  :root {
    --dark-blue: #1f3a93;
    --mid-blue: #1a6fc4;
    --light-blue: #2a8ad8;
    --orange: #f0622d;
    --orange-deep: #e4521f;
    --panel: #f1f5f9;
    --panel-edge: #dde9f5;
    --ink-grey: #6b6b6b;
    --page: #eceff2;
    --white: #ffffff;
  }
  * { box-sizing: border-box; margin: 0; padding: 0; }
  html, body { width: 950px; height: 1200px; overflow: hidden; background: var(--page); }
  .flyer {
    position: absolute; left: 130px; top: 62px; width: 690px; height: 1075px;
    overflow: hidden; background: var(--panel);
    box-shadow: 0 4px 14px rgba(0,0,0,.18);
  }
  .flyer-art { position: absolute; inset: 0; width: 690px; height: 1075px; }
  .brand-name {
    position: absolute; left: 40px; top: 440px; width: 440px; text-align: center;
    font-family: "Montserrat", sans-serif; font-weight: 600; font-size: 37px;
    color: var(--mid-blue); letter-spacing: -0.5px;
  }
  .slogan {
    position: absolute; left: 40px; top: 495px; width: 440px; text-align: center;
    font-family: "Montserrat", sans-serif; font-weight: 300; font-size: 17px;
    color: var(--orange); letter-spacing: 1px;
  }
  .promise {
    position: absolute; left: 21px; top: 606px;
    font-family: "Open Sans", sans-serif; font-style: italic; font-size: 20.5px;
    line-height: 31px; color: var(--orange);
  }
  .perks { position: absolute; left: 21px; top: 688px; list-style: none; }
  .perks li {
    display: flex; align-items: center; height: 49px;
    font-family: "Fira Sans Condensed", sans-serif; font-weight: 500; font-size: 22px;
    color: var(--dark-blue);
  }
  .perks svg { width: 30px; height: 26px; margin-right: 14px; }
  .coupon {
    position: absolute; left: 315px; top: 590px; width: 352px; height: 235px;
    text-align: center; color: var(--white); font-family: "Open Sans", sans-serif;
  }
  .coupon-care { position: absolute; left: 96px; top: 22px; }
  .coupon-headline { position: absolute; top: 50px; width: 100%; font-size: 22px; }
  .coupon-headline strong { font-size: 36px; font-weight: 700; }
  .coupon-code {
    position: absolute; left: 25px; top: 106px; width: 300px; height: 38px;
    background: var(--white); color: var(--ink-grey); font-size: 21px; line-height: 38px;
  }
  .coupon-bonus { position: absolute; top: 150px; width: 100%; font-size: 28px; font-weight: 700; }
  .coupon-limit { position: absolute; top: 190px; width: 100%; font-size: 19px; }
  .cta {
    position: absolute; left: 0; top: 1010px; width: 690px; text-align: center;
    font-family: "Fira Sans Condensed", sans-serif; font-weight: 600; font-size: 27px;
    color: var(--white);
  }
</style>
</head>
<body>
<main class="flyer">
  <svg class="flyer-art" viewBox="0 0 690 1075" aria-hidden="false">
    <defs>
      <linearGradient id="shirts" x1="0" y1="0" x2="1" y2="0">
        <stop offset="0" stop-color="#c9d9ee"/>
        <stop offset=".3" stop-color="#e9eef6"/>
        <stop offset=".5" stop-color="#3e5a8a"/>
        <stop offset=".7" stop-color="#5a85c2"/>
        <stop offset="1" stop-color="#d9e4f2"/>
      </linearGradient>
      <linearGradient id="panel" x1="0" y1="0" x2="1" y2="0">
        <stop offset="0" stop-color="var(--panel-edge)"/>
        <stop offset=".5" stop-color="var(--panel)"/>
        <stop offset="1" stop-color="var(--panel-edge)"/>
      </linearGradient>
    </defs>
    <rect class="shirt-photo" role="img" aria-label="Photo of freshly laundered dress shirts hanging on wooden hangers" x="0" y="0" width="690" height="340" fill="url(#shirts)"/>
    <path class="top-wave-dark" d="M0,250 C140,300 300,330 430,300 C540,275 620,285 690,295 L690,320 C610,305 530,300 430,322 C300,352 140,330 0,300 Z" fill="var(--dark-blue)"/>
    <path class="panel" d="M0,300 C140,330 300,352 430,322 C530,300 610,305 690,320 L690,1075 L0,1075 Z" fill="url(#panel)"/>
    <path class="top-wave-light" d="M0,292 C140,322 300,344 430,314 C530,292 610,297 690,312" fill="none" stroke="var(--light-blue)" stroke-width="4"/>
    <circle class="logo-disc" cx="258" cy="360" r="140" fill="var(--white)"/>
    <path class="logo-arc" d="M122,330 A140,140 0 0 1 396,340" fill="none" stroke="var(--orange)" stroke-width="7"/>
    <path class="coupon-card" d="M329,590 L372,590 L368,542 L420,590 L653,590 Q667,590 667,604 L667,811 Q667,825 653,825 L329,825 Q315,825 315,811 L315,604 Q315,590 329,590 Z" fill="var(--orange)"/>
    <rect x="325" y="600" width="332" height="215" rx="9" fill="none" stroke="var(--white)" stroke-width="1.5" stroke-dasharray="5 4"/>
    <circle class="partner-badge" cx="380" cy="884" r="32" fill="#5f8fc4"/>
    <circle class="partner-badge" cx="480" cy="884" r="35" fill="#f5c518"/>
    <rect class="partner-badge" x="572" y="857" width="38" height="52" rx="6" fill="#111"/>
    <path class="bottom-wave-light" d="M0,935 C160,900 330,925 470,945 C570,958 640,930 690,905 L690,1075 L0,1075 Z" fill="var(--light-blue)"/>
    <path class="bottom-wave-dark" d="M0,960 C170,925 340,950 480,965 C580,975 640,955 690,930 L690,1075 L0,1075 Z" fill="var(--dark-blue)"/>
    <path class="cta-band" d="M0,985 C180,965 360,975 500,985 C590,990 650,980 690,970 L690,1075 L0,1075 Z" fill="var(--mid-blue)"/>
  </svg>

  <div class="brand-name">QuickRinseHub.com</div>
  <p class="slogan">Cleaner. Brighter. Faster.</p>

  <p class="promise">We offer the cleanest and<br>brightest laundry in the city!</p>
  <ul class="perks">
    <li><svg viewBox="0 0 30 26"><rect x="2" y="5" width="19" height="19" fill="none" stroke="var(--orange)" stroke-width="2.5"/><path d="M6,13 L11,19 L27,2" fill="none" stroke="var(--orange)" stroke-width="3"/></svg>FREE pickup and delivery</li>
    <li><svg viewBox="0 0 30 26"><rect x="2" y="5" width="19" height="19" fill="none" stroke="var(--orange)" stroke-width="2.5"/><path d="M6,13 L11,19 L27,2" fill="none" stroke="var(--orange)" stroke-width="3"/></svg>FREE next day service</li>
    <li><svg viewBox="0 0 30 26"><rect x="2" y="5" width="19" height="19" fill="none" stroke="var(--orange)" stroke-width="2.5"/><path d="M6,13 L11,19 L27,2" fill="none" stroke="var(--orange)" stroke-width="3"/></svg>FREE Brisa and Plumo</li>
  </ul>

  <section class="coupon">
    <svg class="coupon-care" width="160" height="22" viewBox="0 0 160 22" fill="none" stroke="#ffd9c8" stroke-width="1.3">
      <path d="M3,6 L19,6 L17,20 L5,20 Z M2,2 L20,21 M20,2 L2,21"/>
      <path d="M32,6 L50,6 L48,20 L34,20 Z"/>
      <rect x="62" y="4" width="16" height="16"/><circle cx="70" cy="12" r="5"/>
      <path d="M92,18 L112,18 L110,8 L98,8 Q94,12 92,18 Z"/>
      <path d="M126,20 L136,3 L146,20 Z M124,3 L148,21 M148,3 L124,21"/>
    </svg>
    <p class="coupon-headline"><strong>50%</strong> your first order</p>
    <p class="coupon-code">coupon code FOLD50</p>
    <p class="coupon-bonus">2nd order FREE!</p>
    <p class="coupon-limit">(up to $50)</p>
  </section>

  <p class="cta">SCHEDULE NOW ON WWW.QUICKRINSEHUB.COM!</p>
</main>
</body>
</html>
```